Icecream Label Design [Merrows Crest]

Our company distributes ice cream in Japan. We produce a private brand that has always been know as Merrows.

However the brand design is poor and we have poor/almost zero brand recognition in the market. Currently people buy our product because it is made in NEW ZEALAND (quality) and represents very good value for money.

BUT

Going forward we want to market Merrows as a 'HIGH QUALITY' icecream BRAND in Japan. We need a package label that reflects this.

We are expanding the current product range (flavour and size) of our Merrow's icecream.

I think this is a great opportunity to get your design exposed in a large Asian market. We have very good distribution channels and will will sell a lot of this ice cream in Japan in the future and the Merrows brand/logo will become well recognized.

Really looking forward to seeing design proposals! Thank you, any questions please ask - PLT
Updates

Project Deadline Extended
Reason: Good morning all. Thank you for submissions. We are wishing to see more examples so have decided to extend the deadline. Looking forward to seeing your ideas. Thanks! Declan

Hi All,

I have sent through the current Merrow's logo. Please feel free to use this logo in your designs if you think it is appropriate. There is also an image of the current label for your reference - emphasis on fresh milk but the overall design is not good hence my request to you all...

Looking forward to your help and further submissions. 

Thanks!

Declan 

Project Deadline Extended
Reason: Just finalizing design. Have extended deadline to accommodate this. Your continued support and cooperation appreciated. Thanks! Declan

Project Deadline Extended
Reason: Finalizing decision being made. Thanks! Declan

Project Deadline Extended
Reason: Will make decision today. Thanks all! Declan

Project Deadline Extended

Target Market(s)

Mother's 30-55 (quality ingredients and value for money)

Industry/Entity Type

It Company

Requirements
Must have
• 1. The brand is Merrows Crest

2. You are designing a logo that will be used on our 1 litre tub and 500ML pottle. Design specification files are attached*.
*Please note: on both the 1L and 500ML tub space must be left for regulatory information. Image attached showing current regulatory information and and space on the 1L tub.

3. We want to use this logo/branding as a base for all our 4 flavour varieties noted below so the design must be able to accommodate this somehow.

4. Needs to have a text placeholder for Japanese translation. ie: if on the design you use text that says 'Vanilla Ice Cream' then somewhere there needs to be space for the Japanese equivalent バニラ アイスクリーム
Nice to have
• 1. Merrows uses 100% fresh milk and cream. It would be nice to convey this somehow.

2. Perhaps could include text 'Your Fresh Taste of New Zealand'

3. There are 4* flavour varieties.
Vanilla | Strawberry | Chocolate | Green Tea
* it would be nice to have a good Merrows base design/pattern which can then be modified slightly (image, colour etc maybe) to reflect each unique flavour.

```html
<!DOCTYPE html>
<html lang="en">
<head>
<meta charset="utf-8">
<title>Merrow's Ice Cream Labels</title>
<link href="https://fonts.googleapis.com/css2?family=Cinzel:wght@400;700&family=Noto+Sans+JP:wght@500&family=Roboto:wght@700&display=swap" rel="stylesheet">
<style>
  :root {
    --page: #ffffff;
    --ink: #1a1a1a;
    --swoosh: #111111;
    --white: #ffffff;
    --green-light: #a4cc5b;
    --green-dark: #1e6934;
    --pink-light: #f2b9c3;
    --pink-dark: #f07ca2;
    --vanilla-light: #e6c97a;
    --vanilla-dark: #c8962f;
    --choc-light: #c49b6d;
    --choc-dark: #3a2317;
  }
  html, body {
    margin: 0;
    width: 1200px;
    height: 900px;
    overflow: hidden;
    background: var(--page);
  }
  .sheet { position: relative; width: 1200px; height: 900px; }
  .shared-defs { position: absolute; width: 0; height: 0; }
  .label { position: absolute; width: 562px; height: 400px; display: block; }
  .label--green    { left: 20px;  top: 36px;  --light: var(--green-light);   --dark: var(--green-dark); }
  .label--pink     { left: 608px; top: 36px;  --light: var(--pink-light);    --dark: var(--pink-dark); }
  .label--vanilla  { left: 20px;  top: 464px; --light: var(--vanilla-light); --dark: var(--vanilla-dark); }
  .label--choc     { left: 608px; top: 464px; --light: var(--choc-light);    --dark: var(--choc-dark); }

  .label__base { fill: var(--light); }
  .label__band { fill: var(--dark); }
  .label__swoosh { fill: var(--swoosh); }
  .label__swoosh-line { fill: none; stroke: var(--light); stroke-width: 4; }
  .brand-name { font-family: "Cinzel", serif; font-weight: 700; font-size: 36px; fill: var(--white); }
  .brand-sub { font-family: "Roboto", Arial, sans-serif; font-weight: 700; font-size: 14px; fill: var(--white); }
  .splash-area { fill: url(#splash-tone); }
  .badge__ring { fill: var(--dark); }
  .badge__core { fill: var(--white); }
  .badge__text { font-family: "Cinzel", serif; font-weight: 700; fill: var(--dark); text-anchor: middle; }
  .badge__pct { font-size: 19px; }
  .badge__line { font-size: 10.5px; }
  .emblem__ring { fill: none; stroke: var(--ink); stroke-width: 2; }
  .emblem__flavour { fill: var(--dark); opacity: .85; }
  .flavour-title { font-family: "Cinzel", serif; font-weight: 700; font-size: 21px; fill: var(--ink); letter-spacing: .5px; }
  .flavour-jp { font-family: "Noto Sans JP", sans-serif; font-weight: 500; font-size: 16px; fill: var(--ink); }
  .tagline { font-family: "Cinzel", serif; font-weight: 400; font-size: 15px; fill: var(--ink); }
</style>
</head>
<body>
<main class="sheet">
  <svg class="shared-defs" aria-hidden="true">
    <defs>
      <path id="arc-title" d="M96.9 278 A96 96 0 1 1 270.2 197.2"/>
      <path id="arc-jp" d="M125 325.3 A110 110 0 0 0 288.3 210.9"/>
      <radialGradient id="orb-shine" cx="0.38" cy="0.32" r="0.75">
        <stop offset="0" stop-color="#6a6a6a"/>
        <stop offset="0.55" stop-color="#1c1c1c"/>
        <stop offset="1" stop-color="#000000"/>
      </radialGradient>
      <radialGradient id="splash-tone" cx="0.5" cy="0.5" r="0.5">
        <stop offset="0" stop-color="#ffffff"/>
        <stop offset="0.7" stop-color="#ffffff" stop-opacity="0.95"/>
        <stop offset="1" stop-color="#ffffff" stop-opacity="0.55"/>
      </radialGradient>
    </defs>
  </svg>

  <!-- Green tea -->
  <svg class="label label--green" viewBox="0 0 562 400" role="group" aria-label="Green tea ice cream label">
    <rect class="label__base" width="562" height="400"/>
    <rect class="label__band" x="390" width="172" height="400"/>
    <path class="label__swoosh" d="M0 0 H340 C310 70 230 110 140 125 C80 135 30 142 0 150 Z"/>
    <path class="label__swoosh-line" d="M0 140 C70 128 240 100 330 8"/>
    <text class="brand-name" x="18" y="56">Merrow's</text>
    <text class="brand-sub" x="20" y="86">High Quality Ice Cream</text>
    <ellipse class="splash-area" role="img" aria-label="Milk splash illustration" cx="380" cy="84" rx="80" ry="74"/>
    <g class="badge">
      <circle class="badge__ring" cx="378" cy="86" r="46"/>
      <circle class="badge__core" cx="378" cy="86" r="39"/>
      <text class="badge__text badge__pct" x="378" y="80">100%</text>
      <text class="badge__text badge__line" x="378" y="96">FRESH MILK</text>
      <text class="badge__text badge__line" x="378" y="109">&amp; CREAM</text>
    </g>
    <circle class="emblem__ring" cx="180" cy="230" r="86"/>
    <g role="img" aria-label="Whipped green tea ice cream with tea leaves">
      <circle cx="180" cy="230" r="70" fill="url(#orb-shine)"/>
      <ellipse class="emblem__flavour" cx="170" cy="262" rx="52" ry="30"/>
    </g>
    <text class="flavour-title"><textPath href="#arc-title">GREEN TEA ICE-CREAM</textPath></text>
    <text class="flavour-jp"><textPath href="#arc-jp">抹茶 アイスクリーム</textPath></text>
    <text class="tagline" x="26" y="372">YOUR FRESH TASTE OF NEW ZEALAND.</text>
  </svg>

  <!-- Strawberry -->
  <svg class="label label--pink" viewBox="0 0 562 400" role="group" aria-label="Strawberry ice cream label">
    <rect class="label__base" width="562" height="400"/>
    <rect class="label__band" x="390" width="172" height="400"/>
    <path class="label__swoosh" d="M0 0 H340 C310 70 230 110 140 125 C80 135 30 142 0 150 Z"/>
    <path class="label__swoosh-line" d="M0 140 C70 128 240 100 330 8"/>
    <text class="brand-name" x="18" y="56">Merrow's</text>
    <text class="brand-sub" x="20" y="86">High Quality Ice Cream</text>
    <ellipse class="splash-area" role="img" aria-label="Milk splash illustration" cx="380" cy="84" rx="80" ry="74"/>
    <g class="badge">
      <circle class="badge__ring" cx="378" cy="86" r="46"/>
      <circle class="badge__core" cx="378" cy="86" r="39"/>
      <text class="badge__text badge__pct" x="378" y="80">100%</text>
      <text class="badge__text badge__line" x="378" y="96">FRESH MILK</text>
      <text class="badge__text badge__line" x="378" y="109">&amp; CREAM</text>
    </g>
    <circle class="emblem__ring" cx="180" cy="230" r="86"/>
    <g role="img" aria-label="Whipped strawberry ice cream with a sliced strawberry">
      <circle cx="180" cy="230" r="70" fill="url(#orb-shine)"/>
      <ellipse class="emblem__flavour" cx="170" cy="262" rx="52" ry="30"/>
    </g>
    <text class="flavour-title"><textPath href="#arc-title">STRAWBERRY ICE-CREAM</textPath></text>
    <text class="flavour-jp"><textPath href="#arc-jp">ストローベリーアイスクリーム</textPath></text>
    <text class="tagline" x="26" y="372">YOUR FRESH TASTE OF NEW ZEALAND.</text>
  </svg>

  <!-- Vanilla -->
  <svg class="label label--vanilla" viewBox="0 0 562 400" role="group" aria-label="Vanilla ice cream label">
    <rect class="label__base" width="562" height="400"/>
    <rect class="label__band" x="390" width="172" height="400"/>
    <path class="label__swoosh" d="M0 0 H340 C310 70 230 110 140 125 C80 135 30 142 0 150 Z"/>
    <path class="label__swoosh-line" d="M0 140 C70 128 240 100 330 8"/>
    <text class="brand-name" x="18" y="56">Merrow's</text>
    <text class="brand-sub" x="20" y="86">High Quality Ice Cream</text>
    <ellipse class="splash-area" role="img" aria-label="Milk splash illustration" cx="380" cy="84" rx="80" ry="74"/>
    <g class="badge">
      <circle class="badge__ring" cx="378" cy="86" r="46"/>
      <circle class="badge__core" cx="378" cy="86" r="39"/>
      <text class="badge__text badge__pct" x="378" y="80">100%</text>
      <text class="badge__text badge__line" x="378" y="96">FRESH MILK</text>
      <text class="badge__text badge__line" x="378" y="109">&amp; CREAM</text>
    </g>
    <circle class="emblem__ring" cx="180" cy="230" r="86"/>
    <g role="img" aria-label="Whipped vanilla ice cream with vanilla pods and flowers">
      <circle cx="180" cy="230" r="70" fill="url(#orb-shine)"/>
      <ellipse class="emblem__flavour" cx="170" cy="262" rx="52" ry="30"/>
    </g>
    <text class="flavour-title"><textPath href="#arc-title">VANILLA ICE-CREAM</textPath></text>
    <text class="flavour-jp"><textPath href="#arc-jp">バニラ アイスクリーム</textPath></text>
    <text class="tagline" x="26" y="372">YOUR FRESH TASTE OF NEW ZEALAND.</text>
  </svg>

  <!-- Chocolate -->
  <svg class="label label--choc" viewBox="0 0 562 400" role="group" aria-label="Chocolate ice cream label">
    <rect class="label__base" width="562" height="400"/>
    <rect class="label__band" x="390" width="172" height="400"/>
    <path class="label__swoosh" d="M0 0 H340 C310 70 230 110 140 125 C80 135 30 142 0 150 Z"/>
    <path class="label__swoosh-line" d="M0 140 C70 128 240 100 330 8"/>
    <text class="brand-name" x="18" y="56">Merrow's</text>
    <text class="brand-sub" x="20" y="86">High Quality Ice Cream</text>
    <ellipse class="splash-area" role="img" aria-label="Milk splash illustration" cx="380" cy="84" rx="80" ry="74"/>
    <g class="badge">
      <circle class="badge__ring" cx="378" cy="86" r="46"/>
      <circle class="badge__core" cx="378" cy="86" r="39"/>
      <text class="badge__text badge__pct" x="378" y="80">100%</text>
      <text class="badge__text badge__line" x="378" y="96">FRESH MILK</text>
      <text class="badge__text badge__line" x="378" y="109">&amp; CREAM</text>
    </g>
    <circle class="emblem__ring" cx="180" cy="230" r="86"/>
    <g role="img" aria-label="Swirled chocolate ice cream with chocolate pieces">
      <circle cx="180" cy="230" r="70" fill="url(#orb-shine)"/>
      <ellipse class="emblem__flavour" cx="170" cy="262" rx="52" ry="30"/>
    </g>
    <text class="flavour-title"><textPath href="#arc-title">CHOCOLATE ICE-CREAM</textPath></text>
    <text class="flavour-jp"><textPath href="#arc-jp">チョコレットアイスクリーム</textPath></text>
    <text class="tagline" x="26" y="372">YOUR FRESH TASTE OF NEW ZEALAND.</text>
  </svg>
</main>
</body>
</html>
```